KV Group

We need a new website for our company and since we had a very good work done for our logo in this site, we're back for the entire job.

Our company name is Marlowe Capital Group. We're adding files of examples of what we have done today. In my opinion we need a more attention lock in the site but yet financial simple work.

Our files (attached) will let you know what we have so far. We need a complete change but the colours should be the same, however you can change them not running away to far from the original, and of course matching with the logo.

We need examples for 3 kind of layouts.

- A HOME welcome layout
- An internal Layout with sidebar
- And internal Layout wide

We can buy image licenses if needed for assets.
Actually there are 5 slide images placed on the Welcome HOME, we need those there, but you can improve with better images to match the new website!!!

Target Market(s)

Clients looking for financial advisers, tax and funds specialist, currency advisers

Industry/Entity Type

Financial

Requirements
Must have
• all the fonts must be in accordance with the financial market sites........the welcome home page must be precise, neat and information accurate........the menu should be elegant........main focus on the Home page, should be also the PRIVATE ACCESS box log in.......

```html
<!DOCTYPE html>
<html lang="en">
<head>
<meta charset="utf-8">
<title>Marlowe Capital Group</title>
<link href="https://fonts.googleapis.com/css2?family=Open+Sans:wght@400;600;700&display=swap" rel="stylesheet">
<style>
:root{
  --orange:#f58220;
  --ink:#222;
  --text:#333;
  --muted:#888;
  --line:#dcdcdc;
  --panel:#f4f4f4;
  --footer:#2b2b2b;
  --footer-text:#8a8a8a;
  --green:#1a8a1a;
  --red:#d01818;
  --navy:#1d2a5a;
}
*{box-sizing:border-box;margin:0;padding:0}
html,body{width:816px;height:1200px;overflow:hidden;background:#fff}
body{position:relative;font-family:"Open Sans",Arial,sans-serif;color:var(--text)}
.abs{position:absolute}
.topline{left:0;top:0;width:816px;height:3px;background:#555}
.brand{left:75px;top:30px;display:flex;align-items:center;gap:8px}
.brand-mark{width:22px;height:22px;background:var(--orange)}
.brand-name{font-size:17px;font-weight:700;color:var(--ink);letter-spacing:.2px}
.btn{height:22px;display:flex;align-items:center;justify-content:center;gap:5px;color:#fff;font-size:8.5px;font-weight:600;border-radius:2px}
.btn-apply{left:569px;top:36px;width:81px;background:var(--ink)}
.btn-contact{left:658px;top:36px;width:84px;background:var(--orange)}
.nav{left:75px;top:90px;width:667px;height:27px;border:1px solid var(--line);display:flex;font-size:9px}
.nav a{display:flex;align-items:center;padding:0 15px;color:var(--text);text-decoration:none;border-right:1px solid var(--line)}
.nav a.active{background:var(--orange);color:#fff;padding:0 15px}
.search{position:absolute;right:13px;top:4px;width:157px;height:18px;border:1px solid var(--line);font-size:6.5px;font-style:italic;color:#aaa;padding:4px 6px}
.search svg{position:absolute;right:5px;top:4px}
.hero{left:75px;top:126px;width:667px;height:233px;background:linear-gradient(110deg,#1b1b1b 0%,#555 45%,#8a8a8a 60%,#3a3a3a 100%)}
.hero-title{left:95px;top:197px;font-size:24px;font-weight:700;color:#fff;line-height:29px;letter-spacing:-.5px}
.hero-btn{left:97px;top:262px;width:72px;height:26px;background:#fff;color:var(--ink);font-size:10px;font-weight:700;display:flex;align-items:center;justify-content:center}
.dots{left:99px;top:341px;display:flex;gap:4px}
.dots span{width:6px;height:6px;border-radius:50%;background:#bbb}
.dots span:first-child{background:var(--orange)}
.access{left:75px;top:368px;width:667px;height:65px;background:var(--panel);border:1px solid #e5e5e5;border-left:3px solid var(--orange)}
.access h2{position:absolute;left:19px;top:8px;font-size:13px;font-weight:600;color:var(--orange)}
.field{position:absolute;top:31px;width:205px;height:20px;background:#e6e6e6;font-size:7.5px;font-style:italic;color:#999;padding:5px 10px;white-space:nowrap;overflow:hidden}
.field-number{left:21px}
.field-password{left:236px}
.forgot{position:absolute;left:457px;top:37px;font-size:6.5px;text-decoration:underline;color:var(--ink);white-space:nowrap}
.login{position:absolute;left:563px;top:28px;width:86px;height:26px;background:var(--orange);color:#fff;font-size:9.5px;font-weight:600;display:flex;align-items:center;justify-content:center}
.welcome{left:75px;top:459px;width:667px}
.welcome h1{font-size:13.5px;font-weight:600;color:var(--ink);margin-bottom:10px}
.welcome p{font-size:8.2px;line-height:13px;margin-bottom:12px}
.card{top:607px;width:196px}
.card .photo{width:196px;height:108px;background:linear-gradient(135deg,#bdbdbd,#4a4a4a)}
.card .head{display:flex;align-items:center;gap:10px;margin-top:19px}
.card .icon{width:30px;height:27px;background:var(--ink);display:flex;align-items:center;justify-content:center}
.card h3{font-size:12px;font-weight:600;color:var(--orange)}
.card p{font-size:7.6px;line-height:10.5px;margin-top:13px;color:var(--ink)}
.card .more{display:block;margin-top:8px;font-size:7.5px;text-decoration:underline;color:var(--ink)}
.ticker{left:75px;top:850px;width:667px;height:40px;background:#f7f7f7;border:1px solid #e6e6e6;overflow:hidden;white-space:nowrap;font-size:6.6px;font-weight:700;color:var(--navy);padding-top:16px}
.ticker span{margin-right:19px}
.up{color:var(--green)}.down{color:var(--red)}.flat{color:var(--orange)}
.verified{left:76px;top:910px;font-size:11px;font-weight:600;color:var(--ink)}
.badge{top:936px;background:#d6d6d6}
.footer{left:75px;top:994px;width:667px;height:197px;background:var(--footer)}
.col{position:absolute;top:15px}
.col h4{font-size:11px;font-weight:600;color:#fff;margin-bottom:6px}
.col li{list-style:none;font-size:7.3px;line-height:12.3px;color:var(--footer-text)}
.copy{position:absolute;left:0;bottom:0;width:667px;height:28px;border-top:1px solid #3a3a3a;font-size:6.6px;color:var(--footer-text);text-align:center;padding-top:9px}
</style>
</head>
<body>
<div class="abs topline"></div>

<div class="abs brand"><div class="brand-mark"></div><div class="brand-name">Marlowe Capital Group</div></div>

<div class="abs btn btn-apply">
  <svg width="9" height="10" viewBox="0 0 9 10"><rect x="1" y="1" width="7" height="8" fill="none" stroke="#fff" stroke-width="1.2"/><path d="M3 4h3M3 6h3" stroke="#fff"/></svg>APPLY NOW</div>
<div class="abs btn btn-contact">
  <svg width="9" height="9" viewBox="0 0 9 9"><path d="M2 1l2 2-1 1 2 2 1-1 2 2-1 1C4 8 1 5 1 2z" fill="#fff"/></svg>CONTACT US</div>

<nav class="abs nav">
  <a class="active">Home</a><a>About Us</a><a>Investments</a><a>Funds</a><a>Brokerage</a><a>Exchange</a><a>Accounts</a>
  <div class="search">Enter your search here...
    <svg width="8" height="8" viewBox="0 0 8 8"><circle cx="3.3" cy="3.3" r="2.4" fill="none" stroke="#333" stroke-width="1.1"/><path d="M5 5l2.3 2.3" stroke="#333" stroke-width="1.3"/></svg></div>
</nav>

<div class="abs hero" role="img" aria-label="Black and white photo of hands joining puzzle pieces"></div>
<div class="abs hero-title">Team Work for your<br>benefit</div>
<div class="abs hero-btn">Read More</div>
<div class="abs dots"><span></span><span></span><span></span><span></span></div>

<section class="abs access">
  <h2>Private Access</h2>
  <div class="field field-number">Please your Account Number</div>
  <div class="field field-password">Please your Account Password</div>
  <span class="forgot">Forgot Acc No. / Password ?</span>
  <div class="login">Log into Acount</div>
</section>

<section class="abs welcome">
  <h1>Welcome to Marlowe Capital Group</h1>
  <p>Le Lorem Ipsum est simplement du faux texte employé dans la composition et la mise en page avant impression. Le Lorem Ipsum est le faux texte standard de l'imprimerie depuis les années 1500.</p>
  <p>Quand un peintre anonyme assembla ensemble des morceaux de texte pour réaliser un livre spécimen de polices de texte. Il n'a pas fait que survivre cinq siècles, mais s'est aussi adapté à la bureautique informatique, sans que son contenu n'en soit modifié. Il a été popularisé dans les années 1960 grâce à la vente de feuilles.On sait depuis longtemps que travailler avec du texte lisible et contenant du sens est source de distractions, et empêche de se concentrer sur la mise en page elle-même.L'avantage du Lorem Ipsum sur un texte générique comme 'Du texte. Du texte. Du texte.' est qu'il possède une distribution</p>
</section>

<article class="abs card" style="left:76px">
  <div class="photo" role="img" aria-label="Black and white overhead photo of a team meeting around a table"></div>
  <div class="head"><div class="icon"><svg width="12" height="12" viewBox="0 0 12 12"><path d="M1 11h10M2 10V2M3 9l6-6M6 3h3v3" fill="none" stroke="#fff" stroke-width="1.3"/></svg></div><h3>Management &amp; Strategy</h3></div>
  <p>Contrairement à une opinion répandue, le Lorem Ipsum n'est pas simplement du texte aléatoire. Il trouve ses racines dans.</p>
  <a class="more">Read More</a>
</article>
<article class="abs card" style="left:311px">
  <div class="photo" role="img" aria-label="Black and white photo of a globe and stacked coins"></div>
  <div class="head"><div class="icon"><svg width="12" height="12" viewBox="0 0 12 12"><rect x="1.5" y="1.5" width="9" height="9" fill="none" stroke="#fff" stroke-width="1.2"/><path d="M7.5 4H5v2h2.5v2H4.5M6 3v6" fill="none" stroke="#fff" stroke-width="1"/></svg></div><h3>Fund</h3></div>
  <p>Contrairement à une opinion répandue, le Lorem Ipsum n'est pas simplement du texte aléatoire. Il trouve ses racines dans.</p>
  <a class="more">Read More</a>
</article>
<article class="abs card" style="left:546px">
  <div class="photo" role="img" aria-label="Black and white photo of hands exchanging banknotes"></div>
  <div class="head"><div class="icon"><svg width="12" height="12" viewBox="0 0 12 12"><path d="M2 5a4 4 0 0 1 7-2M10 7a4 4 0 0 1-7 2" fill="none" stroke="#fff" stroke-width="1.4"/><path d="M8 1l2 2-2 1M4 11L2 9l2-1" fill="#fff"/></svg></div><h3>Currency Exchange</h3></div>
  <p>Contrairement à une opinion répandue, le Lorem Ipsum n'est pas simplement du texte aléatoire. Il trouve ses racines dans.</p>
  <a class="more">Read More</a>
</article>

<div class="abs ticker">
  <span>GBP/UAH = <b class="up">12.65761 ▲</b></span><span>GBP/UGX = <b class="down">4010.06174 ▼</b></span><span>GBP/USD = <b class="up">1.55817 ▲</b></span><span>GBP/UYU = <b class="up">34.36026 ▲</b></span><span>GBP/VEF = <b class="flat">0</b></span><span>GBP/VUV = <b class="up">151</b></span><span>GBP/UAH = <b class="up">12.65761 ▲</b></span>
</div>

<div class="abs verified">Verified &amp; Protected by</div>
<div class="abs badge" style="left:78px;width:73px;height:28px"></div>
<div class="abs badge" style="left:268px;width:100px;height:28px"></div>
<div class="abs badge" style="left:475px;top:928px;width:44px;height:44px;border-radius:50%"></div>
<div class="abs badge" style="left:653px;width:88px;height:28px"></div>

<footer class="abs footer">
  <div class="col" style="left:15px"><h4>About Us</h4><ul><li>History</li><li>Expertize</li><li>Identify</li><li>Strategy</li><li>Contact Us</li></ul></div>
  <div class="col" style="left:125px"><h4>Investment</h4><ul><li>Term Deposits</li><li>Management &amp; Strategy</li><li>Client Relations</li><li>Financial Privacy</li><li>Tax Advice</li><li>Wealth Analysis &amp; Financial Planning</li><li>Active Advisory Group</li><li>Active Advisory Group</li><li>Manager Selection Services</li><li>Private Equity</li></ul></div>
  <div class="col" style="left:311px"><h4>Funds</h4><ul><li>Overview</li><li>Administration</li><li>Funds Security</li><li>Core Services</li><li>Reporting</li><li>Revenue Opportunities</li><li>How it works?</li><li>Glossary</li></ul></div>
  <div class="col" style="left:441px"><h4>Currency Exchange</h4><ul><li>Foreign Exchange</li><li>Fx Forward</li><li>Fx Options</li></ul>
    <h4 style="margin-top:12px">Account</h4><ul><li>Apply Now</li><li>Private Access</li></ul></div>
  <div class="col" style="left:593px"><h4>Brokerage</h4><ul><li>Institutional</li><li>Research</li><li>Trading</li></ul></div>
  <div class="copy">© Copyrights 2013 All rights Reserved</div>
</footer>
</body>
</html>
```